Freelance Writer Letterhead Design

I need business letterhead designed for my freelance public relations/writing company in Denver, Colorado. I write and create articles, white papers, blogs and enewsletters for trade associations, health care organizations and foundations. I already have three versions of my logo in three colors. I would like the design to be executed in the three different colors, so I can use them in various ways. The final design should communicate professionalism, creativity and intellectual work. I want clients to think, "She is smart, professional, creative and more polished than the typical freelance writer; she looks like an agency, but is an individual."

Target Market(s)

Healthcare consulting firms, Foundations,

Industry/Entity Type

Communications

Font styles to use
Other font styles liked:
• Avenir.ttc and Outage.ttf are used in the logo

Requirements
Must have
• The logo
• I'd like it also to have as part of the design, these elements:
• Address: 4876 W. Tamsin Lane, #317, Denver, CO 80231
• Website: www.quillpostmedia-llc.com
• contact information: ingrid@quillpostmedia-llc.com
• phone: 303-555-0184
Nice to have
• a band of color at the bottom or along the sides, using the logo colors

```html
<!DOCTYPE html>
<html lang="en">
<head>
<meta charset="utf-8">
<title>Quillpost Media — Letterhead</title>
<link rel="stylesheet" href="https://fonts.googleapis.com/css2?family=Arimo:wght@400&family=Nunito+Sans:wght@800&display=swap">
<style>
  :root {
    --brand-blue: #3a7dbf;
    --ring-tint: #e9f0f7;
    --ink: #1c1c1c;
    --frame: #8a8a8a;
    --paper: #ffffff;
  }
  html, body {
    margin: 0;
    padding: 0;
    width: 849px;
    height: 1200px;
    overflow: hidden;
    background: var(--paper);
  }
  .letterhead {
    position: relative;
    width: 849px;
    height: 1200px;
    box-sizing: border-box;
    border: 1px solid var(--frame);
    background: var(--paper);
    overflow: hidden;
  }
  .backdrop-ring {
    position: absolute;
    left: 0;
    top: 0;
    width: 849px;
    height: 1200px;
  }
  .wordmark {
    position: absolute;
    left: 51px;
    top: 62px;
    display: flex;
    align-items: center;
    gap: 14px;
  }
  .wordmark-dot {
    width: 38px;
    height: 38px;
    border-radius: 50%;
    background: var(--brand-blue);
  }
  .wordmark-name {
    font-family: "Nunito Sans", sans-serif;
    font-weight: 800;
    font-size: 34px;
    letter-spacing: 0.5px;
    color: var(--brand-blue);
    line-height: 1;
  }
  .contact {
    position: absolute;
    left: 499px;
    top: 45px;
    margin: 0;
    font-family: "Arimo", sans-serif;
    font-style: normal;
    font-size: 15px;
    line-height: 19px;
    color: var(--ink);
  }
  .contact span { display: block; }
</style>
</head>
<body>
  <main class="letterhead">
    <svg class="backdrop-ring" viewBox="0 0 849 1200" aria-hidden="true">
      <circle cx="643" cy="997" r="340" fill="none" stroke="var(--ring-tint)" stroke-width="41"/>
    </svg>

    <header class="wordmark">
      <div class="wordmark-dot" aria-hidden="true"></div>
      <div class="wordmark-name">Quillpost Media</div>
    </header>

    <address class="contact">
      <span class="contact-address">4876 W. Tamsin Lane, #317, Denver, CO 80231</span>
      <span class="contact-phone">303-555-0184</span>
      <span class="contact-web">www.quillpostmedia-llc.com</span>
      <span class="contact-email">ingrid@quillpostmedia-llc.com</span>
    </address>
  </main>
</body>
</html>
```